Flyer-Design für Designer-Schmuck
Großartig - sehr gut !! Super zu frieden !!
Zielgruppe
Wir produzieren außergewöhnlichen und hochwertigen Designer-Schmuck aus Lüster-Bleikristallen für eine modebewusstes Publikum. Der Flyer wird als Beipack-Flyer unseren Versendungen beigefügt und enthält Informationen, sowie Hinweise für unsere Kunden über Morgenfalter, zu Nachhaltigkeit und Pflege.
Aufgabenstellung
nicht größer als DIN A5 | mindestens 2 oder mehr Seiten | Sollte die Aufteilung der Texte 6 Seiten erfordern sind auch 6 Seiten in Ordnung | Design und Layout sind sonst wenig Grenzen gesetzt - wir lassen uns gerne von Euren Vorschlägen begeistern, gerne aber mit Wiedererkennungswert zur Webseite https://morgenfalter-hamburg.de

```html
<!DOCTYPE html>
<html lang="de">
<head>
<meta charset="utf-8">
<title>Morgenfalter – Beipack-Flyer</title>
<link rel="stylesheet" href="https://fonts.googleapis.com/css2?family=Lato:wght@400;700&family=Open+Sans:wght@600;700&display=swap">
<style>
  :root {
    --page-bg: #efe9e3;
    --purple: #8a3c93;
    --purple-soft: #a774ad;
    --text: #3d3a3d;
    --panel-white: #ffffff;
    --panel-light: #f3f2f4;
    --panel-grey: #d8d7d7;
    --note-border: #8a3c93;
  }
  * { box-sizing: border-box; margin: 0; padding: 0; }
  html, body { width: 1200px; height: 820px; overflow: hidden; }
  body {
    background: var(--page-bg);
    font-family: "Lato", sans-serif;
    color: var(--text);
    display: flex;
    align-items: center;
    justify-content: center;
  }
  .flyer {
    width: 1110px;
    height: 572px;
    display: grid;
    grid-template-columns: repeat(3, 1fr);
  }
  .panel { position: relative; display: flex; flex-direction: column; overflow: hidden; }
  .panel--overview { background: var(--panel-white); }
  .panel--promise { background: var(--panel-light); padding: 28px 30px 22px; }
  .panel--care { background: var(--panel-grey); }
  .panel__top { height: 305px; padding: 28px 30px 0; }
  .panel__heading {
    font-family: "Open Sans", sans-serif;
    font-weight: 600;
    color: var(--purple);
    text-transform: uppercase;
    text-align: center;
    font-size: 20px;
    line-height: 1.2;
    margin-bottom: 22px;
  }
  .panel--care .panel__heading { color: #2a282a; }
  .lead { color: var(--purple); font-size: 11px; margin-bottom: 14px; }
  .bullets { list-style: none; font-size: 10.5px; line-height: 1.5; }
  .bullets li::before { content: "• "; }
  .copy { font-size: 10.5px; line-height: 1.5; text-align: justify; }
  .copy p { margin-bottom: 10px; }
  .copy .bullets { margin-bottom: 12px; }
  .photo { flex: 1; }
  .photo--portrait-light { background: linear-gradient(135deg, #f4f1ef 0%, #e3dcd8 55%, #cdbfb8 100%); }
  .photo--portrait-dark { background: radial-gradient(circle at 45% 45%, #4a3a36 0%, #241c1b 55%, #141010 100%); }
  .note {
    margin-top: auto;
    border: 1.5px dashed var(--note-border);
    padding: 10px 12px;
    font-size: 9.5px;
    line-height: 1.45;
    color: var(--purple-soft);
  }
  .note__title { text-transform: uppercase; font-weight: 700; color: var(--purple); margin-bottom: 3px; }
</style>
</head>
<body>
  <main class="flyer">
    <section class="panel panel--overview">
      <div class="panel__top">
        <h2 class="panel__heading">Die Morgenfalter-<br>Schmuckstücke auf einen Blick</h2>
        <p class="lead">Die grazilsten Schmuckstücke von Morgenfalter Hamburg</p>
        <ul class="bullets">
          <li>werden von Hand gefertigt</li>
          <li>sind unverwechselbare Einzelstücke</li>
          <li>werden aus echten Kristallen und 925er Sterlingsilber hergestellt</li>
          <li>erreichen dich in einem speziellen Etui zur schonenden Aufbewahrung</li>
          <li>werden unter hohen Anforderungen an Nachhaltigkeit produziert</li>
        </ul>
      </div>
      <div class="photo photo--portrait-light" role="img" aria-label="Porträt einer Frau mit hellem Haar und rotem Kristallohrring"></div>
    </section>

    <section class="panel panel--promise">
      <h2 class="panel__heading">Unser Nachhaltigkeits-<br>versprechen</h2>
      <div class="copy">
        <p>Es ist uns wichtig, unseren Beitrag zu den hohen Klimazielen unseres Landes zu leisten. Deshalb setzen wir bei Morgenfalter Hamburg folgende Maßnahmen für mehr Nachhaltigkeit um:</p>
        <ul class="bullets">
          <li>Unsere Schmuckstücke bestehen zum großen Teil aus wiederverwendeten Kristallen.</li>
          <li>Die Fassung in Form eines Lüsters wird regional angefertigt.</li>
          <li>Das dekorative Morgenfalter-Etui kannst du auch anderweitig nutzen, um weitere Lieblingsstücke aufzubewahren, oder du kannst es wie gewohnt recyceln.</li>
          <li>Die Schmuckplatten, auf denen du deine Schmuckstücke erhältst, sind aus Acryl gegossen. Wenn du sie nicht benötigst, kannst du sie an uns zurücksenden. Wir verwenden sie dann als Muster oder für Ausstellungsstücke.</li>
          <li>Alle Versandkartons bestehen aus recyceltem Altpapier oder aus Secondhand-Kartonage.</li>
          <li>Grauzonen führen wir selbst durch – dadurch entfallen unnötige Transportwege.</li>
        </ul>
        <p>Wir verbessern unsere Prozesse immer weiter, sodass du deine Morgenfalter-Schmuckstücke nicht nur aus Freude, sondern auch mit gutem Gewissen tragen kannst.</p>
      </div>
      <aside class="note">
        <p class="note__title">Bitte beachte</p>
        <p>Die Kristalle können aufgrund ihres Alters kleinere Gebrauchsspuren aufweisen. Diese sind Teil ihrer Vergangenheit und machen sie nicht weniger schön, sondern verleihen ihnen im Gegenteil eine authentische, lebendige Einzigartigkeit.</p>
      </aside>
    </section>

    <section class="panel panel--care">
      <div class="panel__top">
        <h2 class="panel__heading">Pflegetipps und<br>Sicherheitshinweise</h2>
        <div class="copy">
          <p>Jedes Schmuckstück kommt im dekorativen Morgenfalter-Etui zu dir, das eine liebevolle Aufbewahrung ermöglicht und Schutz vor äußeren Einflüssen bietet. So bleiben die Schönheit und der Glanz deiner Schmuckstücke lange erhalten.</p>
          <p>Ist das Silber doch einmal angelaufen, kannst du ein Silberputztuch oder ein Silberbad verwenden, um es wieder strahlen zu lassen. Die Kristalle werden dadurch nicht geschädigt. Nur Perlen müssen vorher abgenommen werden. Wende dich bei Fragen gern an uns!</p>
          <p>Wichtig: Da die Schmuckstücke verschluckbare Kleinteile enthalten, bewahre sie bitte außerhalb der Reichweite von Kindern unter drei Jahren auf. Kristall und Glas sind zerbrechlich und müssen vor Stoß und Schlag geschützt werden.</p>
        </div>
      </div>
      <div class="photo photo--portrait-dark" role="img" aria-label="Porträt einer Frau mit dunkler Haut und violettem Kristallschmuck vor dunklem Hintergrund"></div>
    </section>
  </main>
</body>
</html>
```